UK Leading HighTech Tooling distributor letterhead

We are one of the UK's leading Engineering Tooling distributers, we are launching our great new catalogue in May and want a red-hot eye catching letterhead to accompany the catalogue.

We want customers who see it to think high quality and premium.

We will roll out the successful style of design accross our other marketing goods (bus cards, website, emails etc) so the winning design will gain more work as a result.

Finally - we are in a rush so please submit quickly your best designs!

Target Market(s)

Precision engineers, senior buyers and managing directors.

Industry/Entity Type

Marketing

Requirements
Must have
• It must feature the Brevix logo as the MAIN logo.
It must have a tag line of 'Complete Tooling Solutions' somewhere on the page.
It should feature our 6 supplier logo's as sub logo's

Contact details:
tel 01632 457203
fax 01632 457204
web brevixparts.example.uk
email sales@brevix.example.net
address : Brevix Ltd, Harlow Yard, Marsh Lane, Eastbrook, Northshire, ZX98 4QP, United Kingdom
Company registration 7481530
Vat no. 518 2407 61
Nice to have
• Bring our logo alive

I have attached an old version of our letterhead so you can see details - please make it much better!

```html
<!DOCTYPE html>
<html lang="en">
<head>
<meta charset="utf-8">
<title>Brevix Letterhead</title>
<link rel="stylesheet" href="https://fonts.googleapis.com/css2?family=Mulish:wght@300;400;700;800&family=Questrial&display=swap">
<style>
  :root {
    --brand-blue: #1b78c2;
    --brand-blue-light: #62aee2;
    --tagline-blue: #4ea3dc;
    --ink: #3f3f3f;
    --ink-soft: #6a6a6a;
    --canvas: #ffffff;
    --sheet: #fbfbfb;
    --sheet-shade: #eceff2;
    --watermark: rgba(27, 120, 194, 0.035);
  }
  * { box-sizing: border-box; margin: 0; padding: 0; }
  html, body {
    width: 1200px; height: 900px; overflow: hidden;
    background: var(--canvas);
    font-family: "Questrial", "Century Gothic", Arial, sans-serif;
    color: var(--ink);
  }
  .sheet {
    position: absolute; left: 286px; top: 0;
    width: 636px; height: 900px; overflow: hidden;
    background: radial-gradient(ellipse at 50% 55%, var(--sheet) 40%, var(--sheet-shade) 100%);
  }
  .sheet-bands { position: absolute; inset: 0; width: 636px; height: 900px; }
  .watermark {
    position: absolute; left: 22px; top: 468px;
    font-family: "Mulish", Arial, sans-serif;
    font-size: 92px; font-weight: 800; letter-spacing: 14px;
    color: var(--watermark);
  }
  .masthead {
    position: absolute; right: 28px; top: 55px;
    display: flex; align-items: center; gap: 16px;
  }
  .tagline {
    font-family: "Mulish", Arial, sans-serif;
    font-size: 18px; font-weight: 300; color: var(--tagline-blue);
    letter-spacing: 0.2px;
  }
  .brand {
    display: flex; align-items: center; gap: 8px;
    font-family: "Mulish", Arial, sans-serif;
    font-size: 26px; font-weight: 800; color: var(--brand-blue);
    letter-spacing: 1.5px;
  }
  .brand-dot {
    width: 22px; height: 22px; border-radius: 50%;
    background: var(--brand-blue);
  }
  .letter {
    position: absolute; left: 75px; top: 158px; width: 488px;
    font-size: 13px; line-height: 15.4px;
  }
  .sender { margin-bottom: 15.6px; }
  .date { margin-bottom: 15.6px; }
  .recipient { margin-bottom: 46.6px; }
  .greeting { margin-bottom: 15.6px; }
  .letter p.body { margin-bottom: 15.6px; }
  .signoff { margin-top: 30px; margin-bottom: 15.6px; }
  .suppliers {
    position: absolute; left: 76px; top: 797px; width: 484px;
    display: flex; justify-content: space-between; align-items: center;
    font-family: "Mulish", Arial, sans-serif;
    font-size: 12px; font-weight: 700; color: var(--ink);
  }
  .supplier { display: flex; align-items: center; gap: 4px; white-space: nowrap; }
  .supplier-mark { width: 10px; height: 10px; background: var(--brand-blue); }
  .supplier-mark.round { border-radius: 50%; }
  .contact {
    position: absolute; left: 75px; top: 835px;
    font-family: "Mulish", Arial, sans-serif;
    font-size: 8.6px; font-weight: 400; color: var(--ink-soft); line-height: 11.5px;
  }
  .contact .sep { color: var(--brand-blue); margin: 0 4px; }
</style>
</head>
<body>
  <main class="sheet">
    <svg class="sheet-bands" viewBox="0 0 636 900" aria-hidden="true">
      <defs>
        <linearGradient id="band" x1="0" y1="0" x2="1" y2="0">
          <stop offset="0" stop-color="#1b78c2"/>
          <stop offset="0.5" stop-color="#62aee2"/>
          <stop offset="1" stop-color="#1b78c2"/>
        </linearGradient>
      </defs>
      <path d="M0 0H636V18C420 16 130 26 0 92Z" fill="url(#band)"/>
      <path d="M0 900V882H420C540 880 600 850 636 810V900Z" fill="url(#band)"/>
    </svg>

    <div class="watermark" aria-hidden="true">BREVIX</div>

    <header class="masthead">
      <span class="tagline">COMPLETE TOOLING SOLUTIONS</span>
      <span class="brand"><span class="brand-dot"></span>BREVIX</span>
    </header>

    <article class="letter">
      <p class="sender">Brevix Ltd, Harlow Yard,<br>Marsh Lane, Eastbrook,<br>Northshire, ZX98 4QP, United Kingdom</p>
      <p class="date">03/16/10</p>
      <p class="recipient">&lt;Recipient Address Goes Here&gt;</p>
      <p class="greeting">Hello.</p>
      <p class="body">Eque cus eat pa erchil idipien daeperchita sim quiam fugitas ut accum hilist, ape reius ducilit fugia quibus remquibus adist ea sum faceatia sum haruptas nis ad que sae etur arit, solorpos ellautem el et apiet faccuscipsus as aut eate nonest que optur?</p>
      <p class="body">Omnima ducipictae pliquid eliqui cone nati quis minulpa dellabores nis net aborum quam, nonsequod que core con necae et hil iur sequi velestis plicid eos re inti autenist, que pro eium nobis molende liquatatur aut minvel is que eosandita qui offici de odit as rem qui bea volorit est quiatibus, eatesed quod eiusa nis est quunt volor aut omnit es­seque quas di dit essinimi, nonse vid min pra con recatur, cus min provitas dolupta plac­caborem quid mo blabore ptatior eprore laccata demod earibus.</p>
      <p class="body">Ficaerem ut aut fuga. Hiciis se nonserovit estotaturita cullectat liquam, volo officto eum enihil et as esendicime non consentiam quiae ent la is est et andusante omniend ipsam, omniam am, saerum quatestis ma in cone latem quunt.</p>
      <p class="signoff">Regards,</p>
      <p class="signature">Name Surname</p>
    </article>

    <footer>
      <div class="suppliers">
        <span class="supplier"><span class="supplier-mark"></span>Tarvo</span>
        <span class="supplier"><span class="supplier-mark round"></span>Lindqvist Inc.</span>
        <span class="supplier"><span class="supplier-mark"></span>Morvane</span>
        <span class="supplier"><span class="supplier-mark round"></span>Halberg</span>
        <span class="supplier"><span class="supplier-mark"></span>Quenby Inc.</span>
        <span class="supplier">Velstrom</span>
      </div>
      <div class="contact">
        T: 01632 457203<span class="sep">|</span>F: 01632 457204<span class="sep">|</span>E: sales@brevix.example.net<span class="sep">|</span>www.brevixparts.example.uk<br>
        Company registration 7481530<span class="sep">|</span>Vat no. 518 2407 61
      </div>
    </footer>
  </main>
</body>
</html>
```